Sports Nutrition Supplement Label design

We need a sports supplement label design for an existing business. (I have provided our business logo in the file uploads) These labels will remain consistent across the product line with the name of the product being the only changing field. The current product names (example: "vegan") on the labels provided are just for reference, the ingredients portions etc are final, but the actual name will be changed to something less generic for each product. I will just need to be able to change the name and have it match with label concept. We would like the look to be professional, clean, and exemplify quality. Please reference our business website tidelinevigor.com to get a feel for design and brand association.
I have also included the NKB supplement label guidelines so we are certain to maintain compliance.
Thank you and I'm looking forward to working with you and seeing your creative designs!
Darin

Target Market(s)

Athletes, Sports professionals, Colleges, Professional Sports Teams

Industry/Entity Type

Sports Science/ Sports Training/Athletics

Requirements
Nice to have
• I would like the design to possibly reflect these key terms: Sport Science, Chemistry, Clean, Professional, Quality (We also like water/ocean/waves concepts but is not a "requirement" it would have to really work well in the design somehow to appeal to wide range of athletes)

```html
<!DOCTYPE html>
<html lang="en">
<head>
<meta charset="utf-8">
<title>Tideline Vigor – Isolate Label</title>
<link rel="stylesheet" href="https://fonts.googleapis.com/css2?family=Oswald:wght@500;700&family=Roboto+Condensed:wght@400;700&family=Roboto:wght@400;500;700&display=swap">
<style>
:root{
  --navy:#0b1d4d;
  --navy-deep:#071436;
  --cyan:#3fd3f0;
  --white:#ffffff;
  --ink:#111111;
  --silver-1:#f4f4f4;
  --silver-2:#9a9a9a;
  --flavor-ink:#1b2f8a;
  --badge:#2d4fa8;
  --badge-alt:#4d7a2a;
}
*{box-sizing:border-box;margin:0;padding:0}
html,body{width:1200px;height:1200px;overflow:hidden;background:var(--white)}
body{font-family:'Roboto',sans-serif;position:relative}
.label{position:absolute;left:20px;top:412px;width:1160px;height:376px;background:var(--navy);color:var(--white);overflow:hidden}
.label-waves{position:absolute;inset:0;background:
  radial-gradient(ellipse 60% 30% at 50% 55%,rgba(63,211,240,.22),transparent 70%),
  linear-gradient(160deg,var(--navy-deep) 0%,var(--navy) 45%,#12306e 60%,var(--navy) 80%)}

.panel-left{position:absolute;left:25px;top:16px;width:272px;font-size:7.4px;line-height:1.3}
.panel-left p{margin-bottom:4px}
.benefits{list-style:none;margin:2px 0 6px}
.benefits li::before{content:"•";margin-right:4px}
.info-box{background:var(--white);color:var(--ink);padding:3px 6px}
.info-box .use{text-align:center;border-bottom:1px solid var(--ink);padding-bottom:3px;margin-bottom:2px}
.amino-title{text-align:center;font-weight:700;font-size:5.4px;margin:2px 0 3px}
.amino{display:grid;grid-template-columns:1fr 1fr;gap:0 14px;font-size:5.4px;line-height:7px;padding:0 8px 3px;border-bottom:1px solid var(--ink);margin-bottom:2px}
.amino .row{display:flex;align-items:baseline;white-space:nowrap}
.amino .leader{flex:1;height:0;border-bottom:1px dotted #888;margin:0 2px;align-self:flex-end;margin-bottom:1.5px}
.warning,.disclaimer{font-size:5.6px;line-height:1.3;padding:2px 0;margin:0!important}
.warning{border-bottom:1px solid var(--ink)}
.disclaimer{font-weight:700}
.lot{margin-top:6px;font-size:7px}
.lot strong{display:block}

.brand{position:absolute;left:525px;top:17px;width:110px;height:60px;background:linear-gradient(180deg,var(--silver-1),var(--silver-2));color:var(--ink);display:flex;align-items:center;justify-content:center;font-weight:500}
.brand .name{font-size:14px;letter-spacing:1.5px;line-height:1.1;text-align:center}
.product-name{position:absolute;left:0;right:0;top:94px;text-align:center;font-family:'Oswald',sans-serif;font-weight:700;font-size:92px;line-height:1;letter-spacing:6px;background:linear-gradient(180deg,#ffffff 0%,#d8d8d8 45%,#8d8d8d 100%);-webkit-background-clip:text;background-clip:text;color:transparent}
.subtitle{position:absolute;left:0;right:0;top:186px;text-align:center;font-family:'Oswald',sans-serif;font-weight:500;font-size:21px;letter-spacing:.5px}
.flavor{position:absolute;left:445px;top:215px;width:270px;height:18px;background:linear-gradient(90deg,#e6e9f2,#ffffff);color:var(--flavor-ink);font-family:'Roboto Condensed',sans-serif;font-size:12px;display:flex;align-items:center;justify-content:center;gap:4px}
.flavor b{font-weight:700}
.claims{position:absolute;left:0;right:0;top:252px;text-align:center;font-family:'Roboto Condensed',sans-serif;font-size:13.5px;line-height:19px}
.net{position:absolute;left:0;right:0;top:347px;text-align:center;font-family:'Roboto Condensed',sans-serif;font-weight:700;font-size:10.5px;letter-spacing:1.5px;color:#dfe4f0}
.net span{border-left:1px solid #dfe4f0;margin-left:5px;padding-left:5px}

.facts{position:absolute;left:861px;top:17px;width:273px;background:var(--white);color:var(--ink);padding:5px 10px 6px}
.facts h2{font-family:'Roboto Condensed',sans-serif;font-weight:700;font-size:29px;line-height:1.05}
.facts .serving{font-size:13.5px;line-height:1.15;border-bottom:4px solid var(--ink);padding-bottom:4px}
.facts table{width:100%;border-collapse:collapse;font-size:7.6px}
.facts th{font-weight:700;text-align:left;padding:3px 0 2px;border-bottom:2px solid var(--ink)}
.facts td{padding:1px 0;line-height:9px;border-bottom:.6px solid #555}
.facts td.amt{text-align:center}
.facts td.dv{text-align:right;width:40px}
.facts .notes{font-size:7.6px;border-top:3px solid var(--ink);margin-top:2px;padding-top:3px;line-height:1.3}

.panel-right{position:absolute;left:861px;top:250px;width:275px;font-size:7px;line-height:1.35}
.badges{display:flex;gap:6px;margin:6px 0 4px}
.badge{width:28px;height:28px;border-radius:50%;background:var(--badge);border:2px solid var(--white)}
.badge.alt{background:var(--badge-alt)}
.distributor{font-weight:700;font-size:8px;line-height:1.2}
</style>
</head>
<body>
<section class="label">
  <div class="label-waves" role="img" aria-label="Flowing blue and cyan wave lines sweeping across the navy label"></div>

  <div class="panel-left">
    <p><b>ISOLATE</b> is made from Ultra-Filtered Whey Isolate that is extremely low fat and lactose.</p>
    <p><b>ISOLATE</b> contains both Papain and Protease for protein absorption, and no cheap ingredients, like Glycine or Taurine, to increase protein levels.</p>
    <p><b>ISOLATE</b> is absorbed immediately, flooding your muscles with key amino acids. This makes <b>ISOLATE</b> the perfect protein to take immediately after your workout, when your muscles crave protein the most.*</p>
    <ul class="benefits">
      <li>25g Protein Per Serving</li>
      <li>0g Added Sugar</li>
      <li>Only 1G of Carbohydrates per Serving</li>
      <li>Digestive Enzymes for Absorption</li>
      <li>100% Whey Isolate</li>
      <li>Cold-Processed, Ultra-Filtered Whey Protein</li>
      <li>Mixes Easily</li>
      <li>Tastes Great</li>
    </ul>
    <div class="info-box">
      <p class="use"><b>Suggested Use</b>: Mix one scoop with 4-6oz of water, milk, or your favorite beverage. Vary the amount of liquid for taste preference.</p>
      <p class="amino-title">Approximate Amino Acids per Serving (Naturally Occurring)</p>
      <div class="amino">
        <div class="row"><span>Alanine</span><span class="leader"></span><span>1514 mg</span></div><div class="row"><span>Arginine</span><span class="leader"></span><span>524 mg</span></div>
        <div class="row"><span>Aspartic Acid</span><span class="leader"></span><span>2941 mg</span></div><div class="row"><span>Cystine</span><span class="leader"></span><span>612 mg</span></div>
        <div class="row"><span>Glutamic Acid</span><span class="leader"></span><span>4019 mg</span></div><div class="row"><span>Glycine</span><span class="leader"></span><span>495 mg</span></div>
        <div class="row"><span>Histidine</span><span class="leader"></span><span>320 mg</span></div><div class="row"><span>Isoleucine*</span><span class="leader"></span><span>1747 mg</span></div>
        <div class="row"><span>Leucine*</span><span class="leader"></span><span>2621 mg</span></div><div class="row"><span>Lysine</span><span class="leader"></span><span>2271 mg</span></div>
        <div class="row"><span>Methionine</span><span class="leader"></span><span>524 mg</span></div><div class="row"><span>Phenylalanine</span><span class="leader"></span><span>757 mg</span></div>
        <div class="row"><span>Proline</span><span class="leader"></span><span>1631 mg</span></div><div class="row"><span>Serine</span><span class="leader"></span><span>1223 mg</span></div>
        <div class="row"><span>Threonine</span><span class="leader"></span><span>1980 mg</span></div><div class="row"><span>Tryptophan</span><span class="leader"></span><span>233 mg</span></div>
        <div class="row"><span>Tyrosine</span><span class="leader"></span><span>641 mg</span></div><div class="row"><span>Valine*</span><span class="leader"></span><span>1572 mg</span></div>
        <div class="row"><span>Total BCAAs</span><span class="leader"></span><span>5940 mg</span></div><div></div>
      </div>
      <p class="warning"><b>Warning</b>: If you have any health conditions, are pregnant, breastfeeding, or taking medication, ask a physician prior to use. Keep out of reach of small children.</p>
      <p class="disclaimer">* These statements have not been evaluated by the NKB. This product is not intended to diagnose, treat, cure or prevent any disease.</p>
    </div>
    <p class="lot">Lot # and Expiration Date Printed on Bottom of Bottle.<strong>SKU:ROC281</strong></p>
  </div>

  <div class="brand"><span class="name">TIDELINE<br>VIGOR</span></div>
  <h1 class="product-name">ISOLATE</h1>
  <p class="subtitle">100% ISOLATE WHEY PROTEIN</p>
  <p class="flavor"><b>Chocolate Milkshake</b> | Natural &amp; Artificial Flavor</p>
  <div class="claims">
    <p>Mixes Easily &amp; Tastes Great</p>
    <p>Digestive Enzymes for Absorption*</p>
    <p>Only 1g of Carbohydrates per Serving</p>
    <p>Cold-Processed, Ultra-Filtered Whey Protein</p>
  </div>
  <p class="net">DIETARY SUPPLEMENT<span>NET WT. 907 G &nbsp;(2 LB)</span></p>

  <div class="facts">
    <h2>Supplement Facts</h2>
    <p class="serving">Serving Size: 29g (1 Scoop)<br>Servings Per Container: 31+</p>
    <table>
      <tr><th>Amount Per Serving</th><th style="text-align:center">% Daily Value**</th><th></th></tr>
      <tr><td>Calories</td><td class="amt">110</td><td class="dv"></td></tr>
      <tr><td>Total Fat</td><td class="amt">1 g</td><td class="dv">1%*</td></tr>
      <tr><td>Total Carbohydrate</td><td class="amt">1 g</td><td class="dv">&lt; 1%*</td></tr>
      <tr><td>Total Sugars</td><td class="amt">&lt; 1 g</td><td class="dv">‡</td></tr>
      <tr><td>Protein</td><td class="amt">25 g</td><td class="dv"></td></tr>
      <tr><td>Calcium</td><td class="amt">118 mg</td><td class="dv">9%</td></tr>
      <tr><td>Chromium</td><td class="amt">2 mcg</td><td class="dv">7%</td></tr>
      <tr><td>Sodium</td><td class="amt">65 mg</td><td class="dv">3%</td></tr>
      <tr><td>Potassium</td><td class="amt">170 mg</td><td class="dv">4%</td></tr>
    </table>
    <p class="notes">**Percent Daily Values are based on a 2,000 calorie diet.<br>‡Daily Value not established.</p>
  </div>

  <div class="panel-right">
    <p><b>Other Ingredients</b>: Whey Protein Isolate, Dutch Cocoa Powder, Natural &amp; Artificial Flavor, Xanthan Gum, Sucralose, Digestive Enzyme Blend (Protease, Papain), BCAA Blend (Leucine, Isoleucine, Valine).<br><b>Contains</b>: Milk, Soy</p>
    <div class="badges">
      <span class="badge"></span><span class="badge alt"></span><span class="badge"></span><span class="badge"></span><span class="badge alt"></span>
    </div>
    <p class="distributor">Distributed By: Company Name<br>Street Address City, ST Zipcode<br>website or phone number</p>
  </div>
</section>
</body>
</html>
```